Event Production Company needs a Poster for a karaoke party

We need a poster similar to the one attached (the same typology of the logo), in which it can be seen that there are three prizes for the winners, a presenter and a jury. The room where the party is held is in Mirtel next Saturday, December 17, 2022. We are looking for an innovative poster, with a youthful air and a desire to party
Target Market(s)
Young people between 16 and 20 years old
Font styles to use
Other font styles liked:
- Pump Triline

Colors
E54698
E96AAD
F1A4CE
F9D9EA
FCEFF6
A7469A
B969AE
D3A5CF
EDDBEB
F8F0F9
6B429C
8869AF
B7A5CE
E3DAEB
F3F0F8
Requirements
Must have
- Fluorescent colors (neon), date, time and day of the event, the instagram profile has to appear

Nice to have
- that the gifts that are offered appear

Should not have
- little relevant information

```html
<!DOCTYPE html>
<html lang="es">
<head>
<meta charset="utf-8">
<title>Glow Karaoke – Mirtel</title>
<link rel="stylesheet" href="https://fonts.googleapis.com/css2?family=Monoton&family=Montserrat:wght@500;600;700&display=swap">
<style>
  :root {
    --page-bg: #b3b3b3;
    --violet-deep: #3a0a8f;
    --violet-mid: #6a0bc4;
    --violet-bright: #a510e2;
    --neon-magenta: #c80fd8;
    --white: #ffffff;
    --brand-red: #9b3540;
    --gift-gold: #d9a443;
    --gift-white: #f4f1f7;
  }
  * { box-sizing: border-box; margin: 0; padding: 0; }
  html, body {
    width: 667px; height: 1200px; overflow: hidden;
    background: var(--page-bg);
    font-family: "Montserrat", Arial, sans-serif;
  }
  .poster {
    position: absolute; left: 0; top: 129px;
    width: 667px; height: 942px; overflow: hidden;
    background: linear-gradient(180deg, var(--violet-deep) 0%, var(--violet-mid) 40%, var(--violet-bright) 65%, var(--violet-mid) 88%, var(--violet-deep) 100%);
    box-shadow: 0 6px 18px rgba(0,0,0,.25);
    color: var(--white);
  }
  .bubbles { position: absolute; inset: 0; }
  .brand {
    position: absolute; left: 188px; top: 46px; width: 291px; height: 59px;
    background: var(--white); border-radius: 7px;
    display: flex; align-items: center; justify-content: center;
    font-weight: 700; font-size: 40px; letter-spacing: 10px;
    color: var(--brand-red); padding-left: 10px;
  }
  .title { position: absolute; left: 0; top: 0; width: 667px; height: 420px; }
  .title text { font-family: "Monoton", "Montserrat", sans-serif; fill: var(--white); }
  .hosts {
    position: absolute; top: 446px; width: 100%; text-align: center;
    font-weight: 600; font-size: 28px; letter-spacing: 2px; line-height: 1;
  }
  .hosts .dash { color: var(--neon-magenta); margin: 0 8px; }
  .details {
    position: absolute; top: 482px; width: 100%; text-align: center;
    font-weight: 600; font-size: 12.5px; letter-spacing: .6px; line-height: 1;
  }
  .details .sep { color: var(--neon-magenta); margin: 0 7px; }
  .gift {
    position: absolute; border-radius: 22px;
    background: radial-gradient(ellipse at 50% 60%, var(--gift-white) 0%, #ece3ef 45%, #e6c98f 80%, rgba(217,164,67,0) 100%);
  }
  .gift-left { left: 40px; top: 553px; width: 161px; height: 181px; }
  .gift-center { left: 239px; top: 520px; width: 189px; height: 214px; }
  .gift-right { left: 475px; top: 579px; width: 139px; height: 155px; }
  .prize {
    position: absolute; top: 747px; width: 149px; height: 36px;
    background: var(--white); border-radius: 5px;
    color: var(--neon-magenta); font-weight: 700; font-size: 25px;
    display: flex; align-items: center; justify-content: center;
  }
  .prize-left { left: 46px; }
  .prize-center { left: 260px; }
  .prize-right { left: 473px; }
  .social {
    position: absolute; top: 812px; width: 100%; text-align: center;
    font-weight: 600; font-size: 18px; letter-spacing: 1.2px; line-height: 1;
  }
  .date {
    position: absolute; left: 46px; top: 854px; width: 576px; height: 44px;
    background: var(--white); border-radius: 5px;
    color: var(--neon-magenta); font-weight: 700; font-size: 22px;
    display: flex; align-items: center; justify-content: center;
  }
</style>
</head>
<body>
  <main class="poster">
    <svg class="bubbles" width="667" height="942" aria-hidden="true">
      <defs>
        <radialGradient id="bubble-fill" cx="0.35" cy="0.65" r="0.7">
          <stop offset="0" stop-color="#e27af5"/>
          <stop offset="1" stop-color="#a812e0"/>
        </radialGradient>
      </defs>
      <circle cx="45" cy="45" r="75" fill="url(#bubble-fill)"/>
      <circle cx="547" cy="5" r="22" fill="url(#bubble-fill)"/>
      <circle cx="670" cy="145" r="65" fill="url(#bubble-fill)"/>
      <circle cx="644" cy="347" r="7" fill="url(#bubble-fill)"/>
      <circle cx="36" cy="448" r="13" fill="url(#bubble-fill)"/>
      <circle cx="60" cy="920" r="95" fill="url(#bubble-fill)" opacity=".6"/>
      <circle cx="663" cy="772" r="18" fill="url(#bubble-fill)"/>
      <circle cx="467" cy="935" r="32" fill="url(#bubble-fill)"/>
    </svg>

    <div class="brand">MIRTEL</div>

    <svg class="title" width="667" height="420" role="img" aria-label="Glow Karaoke">
      <defs>
        <filter id="neon-glow" x="-10%" y="-20%" width="120%" height="140%">
          <feGaussianBlur stdDeviation="4" result="blur"/>
          <feFlood flood-color="#e27af5"/>
          <feComposite in2="blur" operator="in"/>
          <feMerge><feMergeNode/><feMergeNode in="SourceGraphic"/></feMerge>
        </filter>
      </defs>
      <text x="147" y="278" font-size="130" textLength="373" lengthAdjust="spacingAndGlyphs" filter="url(#neon-glow)">glow</text>
      <text x="53" y="405" font-size="130" textLength="560" lengthAdjust="spacingAndGlyphs" filter="url(#neon-glow)">Karaoke</text>
    </svg>

    <p class="hosts"><span class="dash">-</span>PRESENTADO POR<span class="dash">-</span></p>
    <p class="details">LARA RUIZ Y NORA VIDAL<span class="sep">|</span>JURADO PROFESIONAL<span class="sep">|</span>+1000€ EN PREMIOS</p>

    <div class="gift gift-left" role="img" aria-label="Ilustración de caja de regalo blanca con lazo dorado, segundo premio"></div>
    <div class="gift gift-center" role="img" aria-label="Ilustración de caja de regalo blanca con lazo dorado, primer premio"></div>
    <div class="gift gift-right" role="img" aria-label="Ilustración de caja de regalo blanca con lazo dorado, tercer premio"></div>

    <div class="prize prize-left">300€</div>
    <div class="prize prize-center">500€</div>
    <div class="prize prize-right">150€</div>

    <p class="social">TODA LA INFO : @GLOWKARAOKE</p>
    <div class="date">SÁBADO, 17 DE DICIEMBRE DE 2022</div>
  </main>
</body>
</html>
```